Surfing fin design company

Design and build a website.Technical scope - SEO optimisation for high impact results. Website will have high quality videos and images but will be quick to download and transition from one page to the next. It will have a selling function with product of the month(advertised on landing page), shop, rotating/zoom images, selection, basket (discount voucher, postage functions) and pay functionality. Functioning membership area with blog, and database for recording all data.... Automatic email function upon; prolonged use time on site, submission of personal data, purchase and drop shipping (variables controlled by admin privileges)Landing page will multiple designs and formats (for future optimisation), scrolling points of interest from different parts of the sites.Style - The website will have an initial landing page with a modern cool surfing vibe/theme but appeal to both surf groms and commercial surf companies. Abstract stock wave images and videosWant to have low/basic technical Admin interface to manage membership, email and content.

Coding

Coded - Design and coding required

Number of Pages Required

5+ page

Colors

Designer to choose colors to be used in the design.

Requirements
Must have
• Must include the company logo attached

```html
<!DOCTYPE html>
<html lang="en">
<head>
<meta charset="utf-8">
<title>Tide Fins — Surf Fins &amp; Boards</title>
<link rel="stylesheet" href="https://fonts.googleapis.com/css2?family=Open+Sans:wght@400;600;700;800&family=Source+Sans+3:wght@400;600;700;800&display=swap">
<style>
:root{
  --blue:#2d9fdc;
  --blue-deep:#1b7fc0;
  --blue-soft:#cfe8f7;
  --navy:#232a36;
  --ink:#161b24;
  --text:#333;
  --muted:#777;
  --line:#e2e2e2;
  --card:#e6e6e6;
  --white:#fff;
  --sea-1:#0f6f8f;
  --sea-2:#3fb7cf;
  --sea-3:#a9e3ee;
}
*{margin:0;padding:0;box-sizing:border-box}
html,body{width:1200px;height:3696px;overflow:hidden}
body{position:relative;background:var(--white);font-family:"Open Sans",sans-serif;color:var(--text)}
.abs{position:absolute}

/* top bar & nav */
.topbar{left:0;top:0;width:1200px;height:35px;background:#eef0f4}
.topbar .call{position:absolute;right:225px;top:10px;font-size:12px;color:var(--blue);font-weight:600}
.topbar .call b{color:var(--navy)}
.topbar .login{position:absolute;right:150px;top:8px;font-size:12px;font-weight:700;color:var(--navy);display:flex;align-items:center;gap:6px}
.topbar .login i{width:18px;height:18px;border:2px solid var(--navy);border-radius:50%;display:block}
.nav{left:0;top:35px;width:1200px;height:69px;background:var(--white)}
.brand{font-family:"Source Sans 3",sans-serif;font-weight:800;font-size:30px;color:var(--blue);display:flex;align-items:center;gap:8px}
.brand i{width:14px;height:14px;background:var(--blue);border-radius:50%;display:block}
.nav .brand{position:absolute;left:150px;top:16px}
.menu{position:absolute;left:603px;top:28px;display:flex;gap:29px;font-size:11px;font-weight:600;color:var(--navy);list-style:none}
.cart{position:absolute;left:1015px;top:26px;width:20px;height:16px}
.cart-count{position:absolute;left:1030px;top:22px;width:16px;height:16px;border-radius:50%;background:var(--blue);color:#fff;font-size:9px;text-align:center;line-height:16px}

/* hero */
.hero{left:0;top:104px;width:1200px;height:560px}
.hero h1{position:absolute;left:150px;top:118px;font-size:33px;line-height:46px;font-weight:800;color:#fff}
.btn{display:inline-block;background:var(--blue);color:#fff;font-size:12px;font-weight:600;border-radius:3px}
.hero .btn{position:absolute;left:150px;top:280px;padding:8px 24px;border-radius:16px}

/* features */
.features{left:150px;top:675px;width:900px;height:104px;display:flex;gap:10px}
.feature{flex:1;border:1px solid var(--line);display:flex;align-items:center;padding-left:32px;gap:22px}
.feature .ico{width:40px;height:40px;border-radius:50%;background:var(--blue);flex:none;display:flex;align-items:center;justify-content:center}
.feature h4{font-size:12px;font-weight:700;color:var(--navy)}
.feature p{font-size:10px;color:var(--muted);margin-top:3px}

/* welcome */
.welcome-panel{left:0;top:838px;width:429px;height:431px;background:var(--blue)}
.welcome-panel h2{position:absolute;left:70px;top:165px;font-family:"Source Sans 3",sans-serif;font-size:40px;line-height:52px;font-weight:700;color:#fff}
.conquer{left:468px;top:878px;width:590px}
.conquer h2{font-family:"Source Sans 3",sans-serif;font-size:39px;font-weight:800;color:var(--navy);letter-spacing:.5px}
.conquer p{font-size:10px;line-height:17px;color:var(--muted);margin-top:12px}
.welcome-photo{left:429px;top:1072px;width:771px;height:394px;background:linear-gradient(160deg,#7fb7c7 0%,#2f6f86 45%,#8fc5d2 75%,#d7ecf0 100%)}
.play{left:785px;top:1237px;width:56px;height:56px;border-radius:50%;background:rgba(255,255,255,.85)}
.arrow-box{left:367px;top:1207px;width:62px;height:62px;background:var(--navy)}

/* sale */
.sale{left:0;top:1518px;width:1200px;height:453px;background:var(--navy)}
.sale h2{position:absolute;left:150px;top:180px;font-family:"Source Sans 3",sans-serif;font-size:41px;font-weight:800;color:#fff}
.sale h3{position:absolute;left:150px;top:228px;font-family:"Source Sans 3",sans-serif;font-size:25px;font-weight:700;color:var(--blue)}
.sale h4{position:absolute;left:150px;top:268px;font-family:"Source Sans 3",sans-serif;font-size:25px;font-weight:700;color:#fff}
.sale .btn{position:absolute;left:150px;top:320px;padding:7px 14px;border-radius:0;font-size:11px}

/* new arrivals */
.section-title{left:0;width:1200px;text-align:center;font-family:"Source Sans 3",sans-serif;font-weight:800;color:var(--navy);font-size:32px}
.arrivals-backdrop{left:150px;top:2156px;width:900px;height:468px;background:linear-gradient(180deg,var(--blue) 0%,var(--blue-soft) 30%,var(--blue-soft) 70%,var(--blue) 100%)}
.product{top:2260px;width:188px;height:258px;background:var(--card);text-align:center}
.product .board{position:absolute;left:74px;top:18px;width:40px;height:172px;border-radius:50%}
.product h5{position:absolute;left:0;right:0;top:202px;font-size:11px;font-weight:600;color:var(--navy)}
.product span{position:absolute;left:0;right:0;top:220px;font-size:11px;color:var(--blue)}

/* blog */
.blog-bg{left:0;top:2760px;width:1200px;height:652px}
.blog-title{top:2862px;color:#fff;font-size:33px}
.post{top:2927px;width:215px;height:345px;background:#fff}
.post .thumb{height:158px}
.post .date{position:absolute;left:10px;top:172px;font-size:9px;color:var(--text)}
.post h5{position:absolute;left:10px;right:10px;top:190px;font-size:12px;line-height:17px;font-weight:700;color:var(--navy)}
.post p{position:absolute;left:10px;right:10px;top:250px;font-size:9px;line-height:14px;color:var(--muted)}
.explore{left:532px;top:3307px;width:136px;height:32px;border:1px solid #fff;color:#fff;font-size:11px;font-weight:600;text-align:center;line-height:30px}

/* footer */
.footer{left:0;top:3412px;width:1200px;height:284px;background:var(--ink);color:#c9ccd2}
.footer .brand{position:absolute;left:150px;top:86px;font-size:30px}
.socials{position:absolute;left:178px;top:138px;display:flex;gap:12px}
.socials i{width:24px;height:24px;border:1px solid #c9ccd2;border-radius:50%;display:block}
.fcol{position:absolute;top:52px}
.fcol h4{font-size:13px;font-weight:700;color:#fff;margin-bottom:14px}
.fcol li{list-style:none;font-size:9px;line-height:27px}
.fcol p{font-size:9px;line-height:15px;width:210px}
.subscribe{display:inline-block;margin-top:14px;background:var(--blue);color:#fff;font-size:10px;padding:8px 18px}
.contact-row{display:flex;align-items:center;gap:12px;font-size:9px;margin-bottom:26px}
.pay{display:flex;gap:12px;margin-top:-6px}
.pay i{width:40px;height:16px;background:#4a5160;display:block}
.copyright{position:absolute;left:0;right:0;top:257px;text-align:center;font-size:9px;color:#fff}
</style>
</head>
<body>

<header class="abs topbar">
  <div class="call">CALL US : <b>555-018-2734</b></div>
  <div class="login"><i></i>LOG IN</div>
</header>

<nav class="abs nav">
  <div class="brand">Tide Fins<i></i></div>
  <ul class="menu"><li>HOME</li><li>SHOP ⌄</li><li>FIND YOUR FIN</li><li>BLOG</li><li>CONTACTS</li></ul>
  <svg class="abs" style="left:980px;top:29px" width="12" height="12" viewBox="0 0 12 12"><circle cx="5" cy="5" r="3.8" fill="none" stroke="#232a36" stroke-width="1.6"/><line x1="8" y1="8" x2="11" y2="11" stroke="#232a36" stroke-width="1.6"/></svg>
  <svg class="cart" viewBox="0 0 20 16"><path d="M1 1h3l2 9h10l2-7H5" fill="none" stroke="#232a36" stroke-width="1.5"/><circle cx="8" cy="14" r="1.4" fill="#232a36"/><circle cx="15" cy="14" r="1.4" fill="#232a36"/></svg>
  <div class="cart-count">0</div>
</nav>

<section class="abs hero">
  <svg width="1200" height="560" viewBox="0 0 1200 560" role="img" aria-label="Kitesurfer riding a breaking ocean wave">
    <defs>
      <linearGradient id="heroSea" x1="0" y1="0" x2="1" y2="1">
        <stop offset="0" stop-color="#0f5f86"/><stop offset=".45" stop-color="#3aa6cf"/><stop offset=".7" stop-color="#cfeaf3"/><stop offset="1" stop-color="#1f86b3"/>
      </linearGradient>
    </defs>
    <rect width="1200" height="560" fill="url(#heroSea)"/>
    <path d="M0 560 L0 545 C220 470 420 420 700 440 C900 455 1050 440 1200 400 L1200 560Z" fill="var(--blue)"/>
    <path d="M0 560 L0 560 C230 490 430 445 700 462 C900 474 1050 460 1200 422 L1200 560Z" fill="#fff"/>
  </svg>
  <h1>Follow Your Passion<br>And Explore The<br>Beauty Of The Sea World</h1>
  <span class="btn">Explore More</span>
</section>

<section class="abs features">
  <div class="feature"><span class="ico"><svg width="20" height="14" viewBox="0 0 20 14"><path d="M1 2h11v8H1zM12 5h4l3 3v2h-7z" fill="#fff"/><circle cx="5" cy="12" r="2" fill="#fff"/><circle cx="15" cy="12" r="2" fill="#fff"/></svg></span><div><h4>FREE SHIPPING</h4><p>On orders over $99</p></div></div>
  <div class="feature"><span class="ico"><svg width="18" height="18" viewBox="0 0 18 18"><path d="M14 9a5 5 0 1 1-2-4" fill="none" stroke="#fff" stroke-width="2"/><path d="M10 2l3 3-4 1z" fill="#fff"/></svg></span><div><h4>ORDER RETURN</h4><p>Returns within 7 days</p></div></div>
  <div class="feature"><span class="ico"><svg width="20" height="14" viewBox="0 0 20 14"><rect x="1" y="1" width="18" height="12" fill="none" stroke="#fff" stroke-width="1.6"/><path d="M1 1l9 7 9-7" fill="none" stroke="#fff" stroke-width="1.6"/></svg></span><div><h4>CONTACT US</h4><p>Contact us for support services</p></div></div>
</section>

<section>
  <div class="abs welcome-panel"><h2>WELCOME TO<br>TIDE FINS</h2></div>
  <div class="abs conquer">
    <h2>CONQUER THE BIGGEST WAVES</h2>
    <p>Lorem ipsum dolor amet, consectetur adipiscing elit. Nullam at enim libero. Praesent tellus enim. Proin lacinia lorem ac metus convallis malesuada. Aenean dictum, nisi ut ultrices tincidunt, lectus metus efficitur lectus, ut vulputate nulla odio nec dolor. Nam eget dolor sed leo luctus tristique. Duis iaculis quis nisl at dignissim. Duis pulvinar, velit quis malesuada dictum, tortor diam rutrum leo, a consequat tortor magna ut urna. Curabitur sit amet nunc pretium, ultrices leo a, egestas nibh. Pellentesque felis diam, maximus ut urna ac, tincidunt dapibus tortor.</p>
  </div>
  <div class="abs welcome-photo" role="img" aria-label="Video still of surfers carrying boards into the surf"></div>
  <svg class="abs play" viewBox="0 0 56 56"><path d="M23 18l15 10-15 10z" fill="var(--blue)"/></svg>
  <svg class="abs arrow-box" viewBox="0 0 62 62"><path d="M28 24l7 7-7 7" fill="none" stroke="#fff" stroke-width="2"/></svg>
</section>

<section class="abs sale">
  <svg class="abs" style="left:0;top:0" width="1200" height="453" viewBox="0 0 1200 453">
    <defs>
      <linearGradient id="salePhoto" x1="0" y1="0" x2="1" y2="1">
        <stop offset="0" stop-color="#3c7f95"/><stop offset=".5" stop-color="#9fd0dc"/><stop offset="1" stop-color="#2a6e86"/>
      </linearGradient>
    </defs>
    <path d="M0 0H1200V0C900 0 760 30 620 95 C470 165 250 150 0 60Z" fill="var(--blue)"/>
    <path d="M0 0H1200V0C900 0 780 15 640 70 C480 135 250 120 0 30Z" fill="#fff"/>
    <path d="M560 0H1200V420C1050 450 850 440 720 360 C640 300 650 120 560 0Z" fill="var(--blue)"/>
    <path d="M590 0H1200V400C1050 430 860 420 740 345 C670 290 670 120 590 0Z" fill="url(#salePhoto)" role="img" aria-label="Surfer in a wetsuit leaping onto a board"/>
  </svg>
  <h2>EXCLUSIVE SALE FOR</h2>
  <h3>SHOP PICKED ITEMS</h3>
  <h4>FLAT 20% OFF</h4>
  <span class="btn">Learn More</span>
</section>

<section>
  <h2 class="abs section-title" style="top:2070px">NEW ARRIVALS</h2>
  <div class="abs arrivals-backdrop" role="img" aria-label="Decorative blue ring ornament behind the product cards"></div>
  <div class="abs product" style="left:150px"><div class="board" role="img" aria-label="White and blue floral surfboard" style="background:linear-gradient(#5b8fd0,#2f5fa8)"></div><h5>Lorem Ipsum Dolor</h5><span>$ 34.99</span></div>
  <div class="abs product" style="left:407px"><div class="board" role="img" aria-label="Blue patterned surfboard" style="background:linear-gradient(#2a6fb8,#e0a04a 50%,#1d4f8f)"></div><h5>Lorem Ipsum Dolor</h5><span>$ 34.99</span></div>
  <div class="abs product" style="left:604px"><div class="board" role="img" aria-label="Navy surfboard with red stripes" style="background:linear-gradient(#1c3e86,#c23a3a 55%,#1c3e86)"></div><h5>Lorem Ipsum Dolor</h5><span>$ 34.99</span></div>
  <div class="abs product" style="left:860px"><div class="board" role="img" aria-label="Wooden surfboard with red stripes" style="background:linear-gradient(#e0a35b,#c0703a 60%,#e0a35b)"></div><h5>Lorem Ipsum Dolor</h5><span>$ 34.99</span></div>
</section>

<section>
  <svg class="abs blog-bg" width="1200" height="652" viewBox="0 0 1200 652" role="img" aria-label="Turquoise curling ocean wave background">
    <defs>
      <linearGradient id="blogSea" x1="0" y1="0" x2="0" y2="1">
        <stop offset="0" stop-color="var(--sea-3)"/><stop offset=".35" stop-color="var(--sea-2)"/><stop offset=".7" stop-color="var(--sea-1)"/><stop offset="1" stop-color="#5fbfd2"/>
      </linearGradient>
    </defs>
    <path d="M0 70C200 10 380 30 560 60 C760 95 950 10 1200 20V652H0Z" fill="url(#blogSea)"/>
  </svg>
  <h2 class="abs section-title blog-title">OUR BLOG</h2>
  <article class="abs post" style="left:150px"><div class="thumb" role="img" aria-label="Surfer on a wave" style="background:linear-gradient(#d9eef4,#4a9bb5)"></div><span class="date">5 February, 2018</span><h5>Maecenas bibendum, massa sollic tudin fringilla velit sed egestas frin gilla.</h5><p>Curabitur suscipit, eros rutrum iaculis vestibulum, mi mi tincidunt ante, sed dignissim urna leo eget velit. Vestibulum vitae iaculis dolor.</p></article>
  <article class="abs post" style="left:379px"><div class="thumb" role="img" aria-label="Group of surfers walking into the sea" style="background:linear-gradient(#c9e4ef,#6aa9bc)"></div><span class="date">5 February, 2018</span><h5>Maecenas bibendum, massa sollic tudin fringilla velit sed egestas frin gilla.</h5><p>Curabitur suscipit, eros rutrum iaculis vestibulum, mi mi tincidunt ante, sed dignissim urna leo eget velit. Vestibulum vitae iaculis dolor.</p></article>
  <article class="abs post" style="left:609px"><div class="thumb" role="img" aria-label="Surfer carrying a board in shallow water" style="background:linear-gradient(#d2e7f0,#7fb4c4)"></div><span class="date">5 February, 2018</span><h5>Maecenas bibendum, massa sollic tudin fringilla velit sed egestas frin gilla.</h5><p>Curabitur suscipit, eros rutrum iaculis vestibulum, mi mi tincidunt ante, sed dignissim urna leo eget velit. Vestibulum vitae iaculis dolor.</p></article>
  <article class="abs post" style="left:838px"><div class="thumb" role="img" aria-label="Row of colourful surfboards" style="background:linear-gradient(90deg,#d8433a,#f0c23a,#3a8fd8,#e86aa0,#f0c23a)"></div><span class="date">5 February, 2018</span><h5>Maecenas bibendum, massa sollic tudin fringilla velit sed egestas frin gilla.</h5><p>Curabitur suscipit, eros rutrum iaculis vestibulum, mi mi tincidunt ante, sed dignissim urna leo eget velit. Vestibulum vitae iaculis dolor.</p></article>
  <div class="abs explore">Explore More</div>
</section>

<footer class="abs footer">
  <div class="brand">Tide Fins<i></i></div>
  <div class="socials"><i></i><i></i><i></i><i></i></div>
  <div class="fcol" style="left:419px"><h4>QUICK LINKS</h4><ul><li>Home</li><li>Find Your Fin</li><li>Blog</li><li>Track My Order</li><li>Contact</li></ul></div>
  <div class="fcol" style="left:582px"><h4>NEWSLETTER</h4><p>Consectetur adipiscing elit. Praesent orci nisi, porta sed diam id, venenatis dignissim urna. Duis sit amet eros a sem viverra mollis nec eu sem.</p><span class="subscribe">➤ Subscribe</span></div>
  <div class="fcol" style="left:862px"><h4>REACH US AT</h4>
    <div class="contact-row"><svg width="16" height="16" viewBox="0 0 16 16"><path d="M4 1l3 3-2 2c1 2 3 4 5 5l2-2 3 3-2 3C7 15 1 9 1 3z" fill="none" stroke="#c9ccd2" stroke-width="1.3"/></svg>Call Us: (555) 0147 882</div>
    <div class="contact-row"><svg width="16" height="12" viewBox="0 0 16 12"><rect x="1" y="1" width="14" height="10" fill="none" stroke="#c9ccd2" stroke-width="1.3"/><path d="M1 1l7 6 7-6" fill="none" stroke="#c9ccd2" stroke-width="1.3"/></svg>Mail Us: hello@tidefins.example</div>
    <div class="pay"><i></i><i></i><i></i></div>
  </div>
  <div class="copyright">© The Tide Fins, All Rights Reserved. Privacy Policy</div>
</footer>

</body>
</html>
```